Business Card for new Architectural Firm

I intend to practice in a rural mountain community in upstate NY, focusing on residential and light commercial projects, including second home / vacation properties. I wish to convey a feeling of rural outdoorsy modernity.

Color is important - bold and urbane. Secondary or tertiary colors preferred.

Font is important, idiosyncratic is ok

Optionally, I may choose to use the name Brackenfold Studio. If used as part of your design, all of the Must Haves are still required.

Images uploaded are logos I like

Industry/Entity Type

Residential

Contact Information for Business Card

Caldwell Prusinski
Architect (This word should stand alone or be associated with my name - not license number)
NY License No. 582163
caldwell@designcpx.com
607 394 2858

Font styles to use
Sans Serif
Decorative

Requirements
Must have
• Whatever files I need to best utilize your design
• PDF
• JPG
• EPS
• Vectorwhatsit
Nice to have
• Logo or element that can be incorporated into other print material.
• Could be a font based card
Should not have
• no clip art
• No templates
• no floor plans
• no building photographs

```html
<!DOCTYPE html>
<html lang="en">
<head>
<meta charset="utf-8">
<title>Business Card Concept — Brackenfold Studio</title>
<link rel="stylesheet" href="https://fonts.googleapis.com/css2?family=Poppins:wght@600&family=Source+Sans+3:wght@400;700&display=swap">
<style>
  :root {
    --bark: #4a3319;
    --bark-deep: #3f2a13;
    --moss: #7aa23f;
    --lichen: #d6e2c6;
    --mist: #eef3e8;
    --paper: #ffffff;
    --ink: #3a2a18;
  }
  * { margin: 0; padding: 0; box-sizing: border-box; }
  html, body { width: 927px; height: 1200px; overflow: hidden; background: var(--paper); }
  body { position: relative; font-family: "Source Sans 3", Arial, sans-serif; color: var(--ink); }

  .sheet-title {
    position: absolute; left: 12px; top: 8px;
    font-size: 27px; font-weight: 700; color: var(--bark);
    letter-spacing: 0.2px;
  }
  .wordmark {
    font-family: "Poppins", "Century Gothic", sans-serif;
    font-weight: 600; color: var(--bark);
    text-transform: uppercase; white-space: nowrap;
  }
  .sheet-mark { position: absolute; right: 14px; top: 10px; font-size: 27px; }

  .size-note { position: absolute; font-size: 14px; color: #222; }

  .card { position: absolute; background: var(--paper); overflow: hidden; }
  .card-band {
    position: absolute; left: 0; top: 0; width: 100%;
    background: linear-gradient(90deg, var(--bark) 0%, #8c7a5e 8%, #c5d2b1 30%, var(--lichen) 55%, #bac7a4 80%, var(--bark-deep) 92%);
    border-bottom: 4px solid var(--moss);
  }
  .card .wordmark { position: absolute; left: 0; width: 100%; text-align: center; }
  .contact {
    position: absolute; display: flex; align-items: center; white-space: nowrap;
  }
  .contact svg { flex: none; fill: var(--moss); }
  .holder { position: absolute; text-align: center; white-space: nowrap; }
  .holder-name { color: var(--ink); }
  .holder-title { color: var(--moss); }

  /* small card */
  .card-small { width: 394px; height: 227px; }
  .card-small .card-band { height: 67px; border-bottom-width: 3px; }
  .card-small .wordmark { top: 75px; font-size: 26px; }
  .card-small .contact { left: 12px; font-size: 13.5px; gap: 8px; }
  .card-small .contact svg { width: 15px; height: 15px; }
  .card-small .holder { left: 212px; width: 160px; }
  .card-small .holder-name { font-size: 18px; }
  .card-small .holder-title { font-size: 12px; margin-top: -3px; }

  .card-a { left: 261px; top: 124px; }
  .card-c { left: 276px; top: 864px; height: 230px; }
  .card-c .card-band { height: 62px; }
  .card-c .card-ground {
    position: absolute; left: 0; top: 65px; width: 100%; height: 165px;
    background: linear-gradient(180deg, #e4ecd9 0%, var(--mist) 55%, #f8faf5 100%);
  }

  /* large card */
  .card-large {
    left: 164px; top: 432px; width: 597px; height: 338px;
    border: 3px solid var(--bark);
  }
  .card-large .card-band { height: 92px; border-bottom-width: 5px; }
  .card-large .wordmark { top: 120px; font-size: 40px; }
  .card-large .contact { left: 28px; font-size: 21px; gap: 13px; }
  .card-large .contact svg { width: 25px; height: 25px; }
  .card-large .holder { left: 330px; width: 240px; }
  .card-large .holder-name { font-size: 30px; }
  .card-large .holder-title { font-size: 18px; margin-top: -2px; }
</style>
</head>
<body>

<svg width="0" height="0" style="position:absolute" aria-hidden="true">
  <symbol id="icon-phone" viewBox="0 0 24 24">
    <path d="M6.6 10.8a15.2 15.2 0 0 0 6.6 6.6l2.2-2.2c.3-.3.7-.4 1-.2 1.1.4 2.3.6 3.6.6.6 0 1 .4 1 1V20c0 .6-.4 1-1 1C10.6 21 3 13.4 3 4c0-.6.4-1 1-1h3.5c.6 0 1 .4 1 1 0 1.3.2 2.5.6 3.6.1.3 0 .7-.2 1z"/>
  </symbol>
  <symbol id="icon-globe" viewBox="0 0 24 24">
    <path fill-rule="evenodd" d="M12 2a10 10 0 1 1 0 20 10 10 0 0 1 0-20zm-1 2.1A8 8 0 0 0 4.1 11H7.5c.1-2.6.6-5 1.5-6.9zm2 0c.9 1.9 1.4 4.3 1.5 6.9h3.4A8 8 0 0 0 13 4.1zM12 4.5c-1 1.7-1.6 4-1.7 6.5h3.4c-.1-2.5-.7-4.8-1.7-6.5zM4.1 13A8 8 0 0 0 9 19.9c-.9-1.9-1.4-4.3-1.5-6.9zm6.2 0c.1 2.5.7 4.8 1.7 6.5 1-1.7 1.6-4 1.7-6.5zm6.2 0c-.1 2.6-.6 5-1.5 6.9a8 8 0 0 0 4.9-6.9z"/>
  </symbol>
  <symbol id="icon-badge" viewBox="0 0 24 24">
    <path fill-rule="evenodd" d="M12 2a10 10 0 1 1 0 20 10 10 0 0 1 0-20zm0 2.2a7.8 7.8 0 1 0 0 15.6 7.8 7.8 0 0 0 0-15.6zM7.6 8.4l1.5-1.5 7.5 8.7-1.5 1.5z"/>
  </symbol>
</svg>

<h1 class="sheet-title">Business Card Concept</h1>
<div class="wordmark sheet-mark">Brackenfold Studio</div>

<p class="size-note" style="left:386px; top:86px;">actual size</p>

<!-- Card A: actual size -->
<section class="card card-small card-a">
  <div class="card-band" role="img" aria-label="Band of slender forest tree trunks in bark brown over pale green"></div>
  <div class="wordmark">Brackenfold Studio</div>
  <div class="contact" style="top:132px;"><svg><use href="#icon-phone"/></svg>607 394 2858</div>
  <div class="contact" style="top:162px;"><svg><use href="#icon-globe"/></svg>NY License No. 582163</div>
  <div class="contact" style="top:192px;"><svg><use href="#icon-badge"/></svg>caldwell@designcpx.com</div>
  <div class="holder" style="top:158px;">
    <div class="holder-name">Caldwell Prusinski</div>
    <div class="holder-title">Architect</div>
  </div>
</section>

<!-- Card B: enlarged -->
<section class="card card-large">
  <div class="card-band" role="img" aria-label="Band of slender forest tree trunks in bark brown over pale green"></div>
  <div class="wordmark">Brackenfold Studio</div>
  <div class="contact" style="top:191px;"><svg><use href="#icon-phone"/></svg>607 394 2858</div>
  <div class="contact" style="top:237px;"><svg><use href="#icon-globe"/></svg>caldwell@designcpx.com</div>
  <div class="contact" style="top:288px;"><svg><use href="#icon-badge"/></svg>NY License No. 582163</div>
  <div class="holder" style="top:238px;">
    <div class="holder-name">Caldwell Prusinski</div>
    <div class="holder-title">Architect</div>
  </div>
</section>

<!-- Card C: actual size, trunks fading down -->
<section class="card card-small card-c">
  <div class="card-ground" role="img" aria-label="Faint tree trunks fading down the card"></div>
  <div class="card-band" role="img" aria-label="Band of slender forest tree trunks in bark brown over pale green"></div>
  <div class="wordmark" style="top:80px;">Brackenfold Studio</div>
  <div class="contact" style="top:130px;"><svg><use href="#icon-phone"/></svg>607 394 2858</div>
  <div class="contact" style="top:159px;"><svg><use href="#icon-globe"/></svg>NY License No. 582163</div>
  <div class="contact" style="top:189px;"><svg><use href="#icon-badge"/></svg>caldwell@designcpx.com</div>
  <div class="holder" style="top:156px;">
    <div class="holder-name">Caldwell Prusinski</div>
    <div class="holder-title">Architect</div>
  </div>
</section>

<p class="size-note" style="left:426px; top:1104px;">actual size</p>

</body>
</html>
```